Brochure for medical doctor

I need a brochure for a medical doctor to promote his practice. The brochure should contain his picture, business information (use letterhead from attachment), and the following text:

- Now accepting PI cases on lien!
- Same and next business day appointments available for initial visits, pre-operative clearances, and all other medical needs

- Expedited medical reports sent quickly to your office

Industry/Entity Type

Medical

```html
<!DOCTYPE html>
<html lang="en">
<head>
<meta charset="utf-8">
<title>Linden Health Clinic – PI Cases Flyer</title>
<link rel="stylesheet" href="https://fonts.googleapis.com/css2?family=Archivo+Black&family=Barlow:wght@400;600;700&display=swap">
<style>
  :root {
    --navy: #3a3f96;
    --green: #1faa63;
    --mint: #e6f5ee;
    --mint-deep: #dff2e8;
    --lavender: #e8e7f8;
    --white: #ffffff;
    --page-bg: #eef1ef;
  }
  html, body {
    margin: 0;
    width: 1200px;
    height: 1200px;
    overflow: hidden;
    background: var(--page-bg);
  }
  .flyer {
    position: absolute;
    left: 190px;
    top: 18px;
    width: 911px;
    height: 1293px;
    transform: scale(0.9);
    transform-origin: top left;
    background: var(--white);
    overflow: hidden;
    font-family: "Barlow", sans-serif;
    color: var(--navy);
  }
  .flyer-shapes, .photo-area { position: absolute; left: 0; top: 0; }
  .brand {
    position: absolute;
    left: 78px;
    top: 86px;
    display: flex;
    align-items: center;
    gap: 16px;
  }
  .brand-mark { width: 62px; height: 62px; background: var(--green); }
  .brand-name {
    font-family: "Barlow", sans-serif;
    font-weight: 700;
    font-size: 31px;
    line-height: 27px;
    color: var(--navy);
    text-transform: uppercase;
  }
  .brand-rule {
    position: absolute;
    left: 78px;
    top: 192px;
    width: 474px;
    height: 1px;
    background: var(--navy);
    opacity: .7;
  }
  .headline {
    position: absolute;
    left: 78px;
    top: 334px;
    margin: 0;
    font-family: "Archivo Black", sans-serif;
    font-weight: 400;
    font-size: 68px;
    line-height: 58px;
    letter-spacing: -1px;
    color: var(--navy);
    text-transform: uppercase;
  }
  .headline .accent { color: var(--green); }
  .services {
    position: absolute;
    left: 78px;
    top: 636px;
    margin: 0;
    padding: 0;
    list-style: none;
  }
  .service {
    position: relative;
    padding-left: 93px;
    font-size: 21px;
    line-height: 26px;
    letter-spacing: .3px;
  }
  .service strong { font-weight: 700; }
  .service-icon { position: absolute; left: 0; top: 50%; transform: translateY(-50%); }
  .service-rule { width: 124px; height: 1px; background: var(--green); margin: 16px 0 16px 93px; }
  .service-tall { min-height: 78px; display: flex; align-items: center; }
  .service-short { min-height: 60px; }
  .contact-title {
    position: absolute;
    left: 78px;
    top: 1114px;
    margin: 0;
    font-weight: 600;
    font-size: 30px;
    color: var(--white);
    text-transform: uppercase;
  }
  .contact-title .accent { color: var(--green); }
  .contact-list {
    position: absolute;
    left: 76px;
    top: 1178px;
    margin: 0;
    padding: 0;
    list-style: none;
    color: var(--white);
    font-size: 17px;
    line-height: 27px;
  }
  .contact-list li { display: flex; align-items: center; gap: 10px; }
  .contact-list strong { font-weight: 600; }
</style>
</head>
<body>
<main class="flyer">
  <svg class="flyer-shapes" width="911" height="1293" viewBox="0 0 911 1293" aria-hidden="true">
    <defs>
      <linearGradient id="band-fade" x1="0" y1="0" x2="1" y2="1">
        <stop offset="0" stop-color="#ffffff"/>
        <stop offset="1" stop-color="#e6e5f8"/>
      </linearGradient>
      <linearGradient id="contact-fill" x1="0" y1="1" x2="1" y2="0">
        <stop offset="0" stop-color="#3d4596"/>
        <stop offset=".55" stop-color="#1f9c6c"/>
        <stop offset="1" stop-color="#1faa63"/>
      </linearGradient>
      <linearGradient id="contact-head" x1="0" y1="0" x2="1" y2="0">
        <stop offset="0" stop-color="#43449a"/>
        <stop offset=".8" stop-color="#3b4f97"/>
        <stop offset="1" stop-color="#3b4f97" stop-opacity="0"/>
      </linearGradient>
    </defs>
    <path d="M0 0 H447 C380 150 230 300 0 318 Z" fill="var(--mint)"/>
    <path d="M0 590 L500 1060 C540 1130 545 1230 520 1293 H0 Z" fill="var(--mint-deep)"/>
    <path d="M0 590 L150 590 L911 1200 L911 1293 L520 1293 C545 1230 540 1130 500 1060 Z" fill="url(#band-fade)"/>
    <path d="M911 175 L911 420 L790 300 Z" fill="var(--green)"/>
    <path d="M470 630 C430 700 430 860 520 935 L560 900 L480 640 Z" fill="var(--green)"/>
    <path d="M0 1100 H477 C525 1170 525 1250 495 1293 H0 Z" fill="url(#contact-fill)"/>
    <path d="M0 1100 H470 L490 1164 H0 Z" fill="url(#contact-head)"/>
    <path d="M505 1080 C560 1150 560 1240 528 1293" fill="none" stroke="var(--mint)" stroke-width="10"/>
  </svg>

  <svg class="photo-area" width="911" height="1293" viewBox="0 0 911 1293" role="img" aria-label="Photo of the doctor in a white coat holding a clipboard">
    <defs>
      <linearGradient id="photo-tone" x1="0" y1="0" x2="0" y2="1">
        <stop offset="0" stop-color="#e4ddd6"/>
        <stop offset="1" stop-color="#f1f1f0"/>
      </linearGradient>
    </defs>
    <path d="M480 85 H860 V1230 L480 850 Z" fill="url(#photo-tone)"/>
  </svg>

  <div class="brand">
    <span class="brand-mark"></span>
    <span class="brand-name">Linden<br>Health<br>Clinic</span>
  </div>
  <div class="brand-rule"></div>

  <h1 class="headline">Now<br>Accepting<br><span class="accent">PI Cases</span><br>On Lien!</h1>

  <ul class="services">
    <li class="service service-tall">
      <svg class="service-icon" width="64" height="58" viewBox="0 0 64 58" aria-hidden="true">
        <rect x="2" y="8" width="50" height="44" rx="3" fill="none" stroke="var(--navy)" stroke-width="3"/>
        <rect x="2" y="8" width="50" height="9" fill="var(--navy)"/>
        <line x1="13" y1="3" x2="13" y2="12" stroke="var(--navy)" stroke-width="3"/>
        <line x1="41" y1="3" x2="41" y2="12" stroke="var(--navy)" stroke-width="3"/>
        <g fill="var(--navy)"><rect x="9" y="23" width="7" height="6"/><rect x="20" y="23" width="7" height="6"/><rect x="9" y="33" width="7" height="6"/><rect x="20" y="33" width="7" height="6"/><rect x="9" y="43" width="7" height="5"/></g>
        <circle cx="48" cy="43" r="12" fill="#fff" stroke="var(--green)" stroke-width="3"/>
        <path d="M48 36 V43 L53 46" fill="none" stroke="var(--navy)" stroke-width="2.5"/>
      </svg>
      <span>Same and next business<br>day appointments<br><strong>available</strong> for initial visits</span>
    </li>
    <li class="service-rule"></li>
    <li class="service service-tall service-short">
      <svg class="service-icon" width="60" height="58" viewBox="0 0 60 58" aria-hidden="true">
        <rect x="3" y="3" width="34" height="34" fill="none" stroke="var(--navy)" stroke-width="2"/>
        <path d="M7 20 H14 L18 12 L23 27 L27 20 H33" fill="none" stroke="var(--green)" stroke-width="2"/>
        <rect x="27" y="20" width="30" height="36" fill="#fff" stroke="var(--navy)" stroke-width="2"/>
        <path d="M32 28 H50 M32 35 H46" stroke="var(--green)" stroke-width="2"/>
        <path d="M35 45 L40 50 L50 40" fill="none" stroke="var(--green)" stroke-width="2.5"/>
      </svg>
      <span>Pre-operative<br><strong>clearances</strong></span>
    </li>
    <li class="service-rule"></li>
    <li class="service service-tall service-short">
      <svg class="service-icon" width="60" height="60" viewBox="0 0 60 60" aria-hidden="true">
        <circle cx="16" cy="16" r="13" fill="none" stroke="var(--navy)" stroke-width="2.5"/>
        <path d="M16 9 V16 H22" fill="none" stroke="var(--navy)" stroke-width="2"/>
        <rect x="20" y="24" width="36" height="32" fill="none" stroke="var(--green)" stroke-width="2"/>
        <path d="M34 32 H42 V38 H48 V44 H42 V50 H34 V44 H28 V38 H34 Z" fill="none" stroke="var(--navy)" stroke-width="2"/>
      </svg>
      <span><strong>Other</strong> medical needs</span>
    </li>
    <li class="service-rule"></li>
    <li class="service service-tall">
      <svg class="service-icon" width="76" height="40" viewBox="0 0 76 40" aria-hidden="true">
        <path d="M2 10 H20 M6 18 H22 M10 26 H22" stroke="var(--navy)" stroke-width="2.5"/>
        <rect x="22" y="5" width="30" height="24" fill="var(--navy)"/>
        <path d="M52 12 H64 L73 22 V29 H52 Z" fill="none" stroke="var(--green)" stroke-width="2.5"/>
        <circle cx="32" cy="32" r="5" fill="#fff" stroke="var(--green)" stroke-width="2.5"/>
        <circle cx="63" cy="32" r="5" fill="#fff" stroke="var(--green)" stroke-width="2.5"/>
      </svg>
      <span>Expedited medical<br>reports <strong>sent quickly</strong><br>to your office</span>
    </li>
  </ul>

  <h2 class="contact-title"><span class="accent">Contact</span> Us</h2>
  <ul class="contact-list">
    <li>
      <svg width="18" height="20" viewBox="0 0 18 20" aria-hidden="true"><path d="M9 1 C4.5 1 2 4.2 2 7.6 C2 12 9 19 9 19 C9 19 16 12 16 7.6 C16 4.2 13.5 1 9 1 Z" fill="#fff"/><circle cx="9" cy="7.5" r="2.6" fill="#3d4596"/></svg>
      <span>4150 Maple Ave. Oak Grove, CA, 90000</span>
    </li>
    <li>
      <svg width="18" height="20" viewBox="0 0 18 20" aria-hidden="true"><path d="M4 2 L7 2 L8 6 L6 8 C7 11 9 13 12 14 L14 12 L17 13 L17 16 C17 17 16 18 15 18 C8 17 3 12 2 4 C2 3 3 2 4 2 Z" fill="none" stroke="#fff" stroke-width="1.8"/></svg>
      <span><strong>Tel:</strong> (555) 014-2200</span>
    </li>
    <li>
      <svg width="20" height="20" viewBox="0 0 20 20" aria-hidden="true"><rect x="5" y="2" width="10" height="5" fill="none" stroke="#fff" stroke-width="1.6"/><rect x="2" y="7" width="16" height="7" rx="1.5" fill="none" stroke="#fff" stroke-width="1.6"/><rect x="5" y="12" width="10" height="6" fill="none" stroke="#fff" stroke-width="1.6"/></svg>
      <span><strong>Fax:</strong> (555) 014-2207</span>
    </li>
  </ul>
</main>
</body>
</html>
```